Luggage and travel essentials company needs Letterhead design (including logo)

Brenmoor luggage is a travel retailer focussed on selling luggage and travel essentials.
We are a company that have a traditional approach to customer service and also embraces the latest technology, especially where it improves the customer experience.
I would like the design to have an airport hint (airport imagery and font preferred), I would also like the colour blue to feature heavily (see attached image for colour hint).
The final design should aim to give the customer confidence that we are dependable and reliable (no script fonts or crazy colours please) but also reflect that we are an innovative and technology focused company.
I would like the letterhead design to include a logo and text.
I am interested in letterhead text containing an embedded logo (much like the 'A' in Zyvanta's logo is also used separately) Note: this is optional.
The text of the letterhead should include the words "Brenmoor Luggage & Travel Essentials", and should include a space for the company phone number, email address, website address along with the company physical address.
Target Market(s)
Affluent Adults aged 25 years and above - Predominantly female
Industry/Entity Type
Airport

```html
<!DOCTYPE html>
<html lang="en">
<head>
<meta charset="utf-8">
<title>Brenmoor Luggage &amp; Travel Essentials — Letterhead</title>
<link href="https://fonts.googleapis.com/css2?family=Arimo:wght@400;700&display=swap" rel="stylesheet">
<style>
  :root {
    --backdrop: #d9d9d9;
    --paper: #ffffff;
    --ink: #2b2b2b;
    --brand-blue: #1b8cc6;
    --brand-blue-light: #8fcbe9;
    --footer-text: #cfe9f7;
    --signature-tone: #e6e6e6;
  }
  * { box-sizing: border-box; margin: 0; padding: 0; }
  html, body {
    width: 1200px; height: 847px; overflow: hidden;
    background: var(--backdrop);
    font-family: "Arimo", Arial, sans-serif;
  }
  .canvas {
    width: 1200px; height: 847px;
    display: flex; align-items: center; justify-content: center;
  }
  .letterhead {
    position: relative;
    width: 599px; height: 847px;
    background: var(--paper);
    color: var(--ink);
  }
  .brand {
    position: absolute; left: 52px; top: 52px;
    display: flex; align-items: center; gap: 10px;
  }
  .brand-dot {
    width: 22px; height: 22px; border-radius: 50%;
    background: var(--brand-blue-light);
  }
  .brand-name {
    color: var(--brand-blue);
    font-weight: 400; font-size: 16px; line-height: 1.2;
  }
  .letter-body {
    position: absolute; left: 52px; right: 52px; top: 140px;
    font-size: 9.4px; line-height: 1.6;
  }
  .salutation { margin-bottom: 12px; }
  .letter-body p.paragraph {
    text-align: justify; margin-bottom: 16px; padding-left: 6px;
  }
  .signature {
    margin-top: 30px; margin-left: 40px;
    width: 150px; height: 40px;
    background: var(--signature-tone);
  }
  .signatory { margin-left: 90px; margin-top: 10px; line-height: 1.35; }
  .footer {
    position: absolute; left: 0; right: 0; bottom: 0; height: 120px;
  }
  .footer svg { position: absolute; inset: 0; }
  .footer-info {
    position: absolute; left: 52px; right: 52px; top: 46px;
    display: flex; gap: 70px;
    font-size: 9.4px; line-height: 1.45; color: var(--paper);
  }
  .footer-info .label { color: var(--footer-text); }
  .footer-info .company { color: var(--footer-text); }
  .company-address { font-style: normal; }
</style>
</head>
<body>
<div class="canvas">
  <article class="letterhead">
    <header class="brand">
      <span class="brand-dot"></span>
      <span class="brand-name">Brenmoor Luggage &amp; Travel Essentials</span>
    </header>

    <section class="letter-body">
      <p class="salutation">Dear Client,</p>
      <p class="paragraph">Lorem ipsum dolor sit amet, consectetur adipisicing elit, sed do eiusmod tempor incididunt ut labore et dolore magna aliqua. Ut enim ad minim veniam, quis nostrud exercitation ullamco laboris nisi ut aliquip ex ea commodo consequat. Duis aute irure dolor in reprehenderit in voluptate velit esse cillum dolore eu fugiat nulla pariatur. Excepteur sint occaecat cupidatat non proident, sunt in culpa qui officia deserunt mollit anim id est laborum.</p>
      <p class="paragraph">Lorem ipsum dolor sit amet, consectetur adipisicing elit, sed do eiusmod tempor incididunt ut labore et dolore magna aliqua. Ut enim ad minim veniam, quis nostrud exercitation ullamco laboris nisi ut aliquip ex ea commodo consequat. Duis aute irure dolor in reprehenderit in voluptate velit esse cillum dolore eu fugiat nulla pariatur. Excepteur sint occaecat cupidatat non proident, sunt in culpa qui officia deserunt mollit anim id est laborum.</p>
      <p class="paragraph">Lorem ipsum dolor sit amet, consectetur adipisicing elit, sed do eiusmod tempor incididunt ut labore et dolore magna aliqua. Ut enim ad minim veniam, quis nostrud exercitation ullamco laboris nisi ut aliquip ex ea commodo consequat. Duis aute irure dolor in reprehenderit in voluptate velit esse cillum dolore eu fugiat nulla pariatur. Excepteur sint occaecat cupidatat non proident, sunt in culpa qui officia deserunt mollit anim id est laborum.</p>
      <div class="signature" role="img" aria-label="Handwritten signature of Adam Hale"></div>
      <p class="signatory">Adam Hale<br>Executive manager</p>
    </section>

    <footer class="footer">
      <svg width="599" height="120" viewBox="0 0 599 120" preserveAspectRatio="none" aria-hidden="true">
        <path d="M0 18 Q300 4 599 10 L599 120 L0 120 Z" fill="var(--brand-blue-light)"/>
        <path d="M0 24 Q300 10 599 16 L599 120 L0 120 Z" fill="var(--brand-blue)"/>
      </svg>
      <div class="footer-info">
        <address class="company-address">
          <span class="company">Brenmoor Luggage &amp; Travel Essentials</span><br>
          48, Market Row, Ashcombe,<br>
          Kent, TN9 4QA
        </address>
        <div class="contact-details">
          <span class="label">phone:</span> 01632 960451<br>
          <span class="label">email:</span> info@brenmoorluggage.co.uk<br>
          www.brenmoorluggage.co.uk
        </div>
      </div>
    </footer>
  </article>
</div>
</body>
</html>
```